Business card design needed

My business is in Matchmaking. My objective is to find the most compatible partner for my clients....basically I'm in the love and happiness industry bringing two people together for a lasting loving relationship.

I envision the design to be something with 2 people who are in love looking happy or even a silhouette.....I don't really know, I'm open to ideas.....maybe no picture at all, but I want it to be classy :-)

I do have a logo which I will upload. You can also go to my website to give you an idea on the colours and the design if that helps, however the website is not finished yet, it should be up by today or tomorrow. If the website has a heart with swirls on the upper left hand corner, that is the old website, please ignore that one. The one that will be up shortly has a picture frame on the home page with my logo that will be in the file I will upload on this page.

Target Market(s)

There are three categories: Over 45, Asian and Western and same sex, but would be able to afford to hire a matchmaker

Contact Information for Business Card

The Tide Lantern
Helping You Find The "One"
Mira Feltham
Matchmaker
0472 915 264
info@thetidelantern.com.au
www.thetidelantern.com.au

```html
<!DOCTYPE html>
<html lang="en">
<head>
<meta charset="utf-8">
<title>The Tide Lantern – Business Card</title>
<link rel="stylesheet" href="https://fonts.googleapis.com/css2?family=Federant&display=swap">
<style>
  :root {
    --teal: #5b9e88;
    --teal-deep: #4e8e79;
    --cream: #eeeee0;
    --plum: #5c4064;
    --plum-soft: #7a5f82;
    --white: #ffffff;
  }
  * { margin: 0; padding: 0; box-sizing: border-box; }
  html, body { width: 741px; height: 1200px; overflow: hidden; }
  body {
    font-family: "Federant", serif;
    background: var(--teal);
  }
  .card {
    position: relative;
    width: 741px;
    height: 1200px;
    overflow: hidden;
    background: radial-gradient(ellipse at 50% 40%, var(--teal) 0%, var(--teal-deep) 100%);
  }
  .frame {
    position: absolute;
    inset: 0;
    width: 741px;
    height: 1200px;
  }
  .brand-mark {
    position: absolute;
    left: 321px;
    top: 66px;
    width: 100px;
    height: 100px;
    border: 4px solid var(--white);
    border-radius: 50%;
  }
  .brand {
    position: absolute;
    top: 200px;
    left: 0;
    width: 741px;
    text-align: center;
    color: var(--white);
    font-size: 44px;
    line-height: 1;
    letter-spacing: 1px;
  }
  .scene {
    position: absolute;
    border-radius: 24px;
    background: radial-gradient(ellipse at center, var(--plum-soft) 0%, rgba(122,95,130,0.55) 60%, rgba(122,95,130,0.15) 100%);
  }
  .scene--hands { left: 298px; top: 372px; width: 136px; height: 136px; }
  .scene--embrace { left: 326px; top: 603px; width: 92px; height: 165px; }
  .scene--proposal { left: 326px; top: 850px; width: 116px; height: 125px; }
  .tagline {
    position: absolute;
    left: 0;
    width: 741px;
    text-align: center;
    color: var(--plum);
    font-size: 36px;
    line-height: 1;
  }
  .tagline--one { top: 522px; }
  .tagline--two { top: 778px; }
  .tagline--three { top: 990px; }
  .contact {
    position: absolute;
    left: 0;
    top: 1110px;
    width: 741px;
    text-align: center;
    color: var(--white);
    font-size: 23px;
    line-height: 30px;
  }
</style>
</head>
<body>
  <main class="card">
    <svg class="frame" viewBox="0 0 741 1200" aria-hidden="true">
      <path fill="var(--cream)" d="M371,287 C392,310 420,330 470,340 C600,360 760,390 790,520 L790,900 C760,1030 600,1050 480,1062 C430,1068 400,1075 371,1088 C342,1075 312,1068 262,1062 C140,1050 -20,1030 -49,900 L-49,520 C-20,390 140,360 272,340 C322,330 350,310 371,287 Z"/>
    </svg>

    <div class="brand-mark" aria-hidden="true"></div>
    <div class="brand">The Tide Lantern</div>

    <div class="scene scene--hands" role="img" aria-label="Silhouette of a couple holding hands"></div>
    <p class="tagline tagline--one">Helping You</p>

    <div class="scene scene--embrace" role="img" aria-label="Silhouette of a couple embracing"></div>
    <p class="tagline tagline--two">Find</p>

    <div class="scene scene--proposal" role="img" aria-label="Silhouette of a man kneeling to propose"></div>
    <p class="tagline tagline--three">The "One"</p>

    <div class="contact">
      <p>Mira Feltham Matchmaker 0472 915 264</p>
      <p>info@thetidelantern.com.au www.thetidelantern.com.au</p>
    </div>
  </main>
</body>
</html>
```